Business Card Design

Need a hot business card in wine colors something cool and mod please feel free to be , FUNKY and free with this .

Industry/Entity Type

Business

Contact Information for Business Card

LUMERA HAIR DESIGN 3182 w 9th st scottsdale az 85619 Custom modern hair design and custom color by MARCUS OBRIDGE 602-4168203 cell salon 480 -712-6084 email marcusobridge@quillpost.com hours wed thru sat 7am to 6pm.

Font styles to use
Other font styles liked:
• something fun and mod.

Colors
a54599
6b449b
1b1b1b
606060

Requirements
Must have
• Apointment reminder on flip side of card.
Should not have
• Nothing boring.

```html
<!DOCTYPE html>
<html lang="en">
<head>
<meta charset="utf-8">
<title>Lumera Hair Design – Business Card</title>
<link rel="stylesheet" href="https://fonts.googleapis.com/css2?family=Stint+Ultra+Condensed&display=swap">
<style>
  :root {
    --wine: #a54599;
    --violet: #6b449b;
    --card: #1b1b1b;
    --grey: #606060;
    --text-grey: #8c8c8c;
    --backdrop: #d3d3d3;
    --font: "Stint Ultra Condensed", serif;
  }
  * { margin: 0; padding: 0; box-sizing: border-box; }
  html, body { width: 1200px; height: 828px; overflow: hidden; }
  body { background: var(--backdrop); position: relative; font-family: var(--font); }

  .card { position: absolute; width: 593px; height: 346px; background: var(--card); overflow: hidden; }
  .card--front { left: 30px; top: 34px; }
  .card--back { left: 545px; top: 431px; }

  .hair-art {
    position: absolute; left: 25px; top: 17px; width: 278px; height: 304px;
    border-radius: 40% 60% 55% 45% / 30% 40% 60% 70%;
    background: linear-gradient(160deg, var(--wine) 0%, var(--wine) 40%, var(--violet) 75%, #3a3a3a 100%);
  }
  .hair-art--faint {
    left: 40px; top: -10px; width: 330px; height: 370px; opacity: 0.12;
    background: linear-gradient(160deg, var(--wine) 0%, var(--violet) 60%, var(--grey) 100%);
  }

  .brand { position: absolute; color: var(--wine); font-family: var(--font); font-weight: 400; text-align: center; line-height: 1; }
  .brand__name { display: block; font-size: 68px; letter-spacing: 3px; }
  .brand__sub { display: block; font-size: 36px; letter-spacing: 1px; margin-top: 2px; }
  .card--front .brand { left: 311px; top: 228px; width: 240px; }
  .card--back .brand { left: 177px; top: 16px; width: 240px; }

  .owner { position: absolute; left: 29px; top: 135px; font-size: 26px; font-weight: 400; color: var(--wine); letter-spacing: 0.5px; }
  .tagline { position: absolute; left: 29px; top: 167px; font-size: 18px; color: var(--text-grey); }

  .contacts { position: absolute; left: 26px; top: 218px; list-style: none; }
  .contacts li { display: flex; align-items: center; height: 27px; font-size: 17px; color: var(--text-grey); }
  .contacts svg { width: 15px; height: 15px; margin-right: 8px; fill: var(--violet); flex: none; }

  .hours { position: absolute; left: 410px; top: 150px; width: 200px; text-align: center; color: var(--text-grey); line-height: 1; }
  .hours__time { font-size: 17px; }
  .hours__time b { font-weight: 400; font-size: 32px; color: var(--wine); }
  .hours__days { font-size: 17px; margin-top: 2px; }
  .hours__days b { font-weight: 400; color: var(--wine); }

  .appointment { position: absolute; left: 331px; top: 201px; width: 236px; }
  .appointment__title, .appointment__label { font-size: 12px; color: var(--violet); letter-spacing: 0.5px; }
  .appointment__label { display: block; margin-top: 8px; }
  .appointment__field { height: 32px; background: var(--grey); border-radius: 3px; margin-top: 3px; }
</style>
</head>
<body>
  <section class="card card--front" aria-label="Card front">
    <div class="hair-art" role="img" aria-label="Flowing wine and violet hair strands with salon scissors"></div>
    <div class="brand">
      <span class="brand__name">LUMERA</span>
      <span class="brand__sub">HAIR DESIGN</span>
    </div>
  </section>

  <section class="card card--back" aria-label="Card back">
    <div class="hair-art hair-art--faint" role="img" aria-label="Faint flowing hair strands and scissors in the background"></div>
    <div class="brand">
      <span class="brand__name">LUMERA</span>
      <span class="brand__sub">HAIR DESIGN</span>
    </div>

    <h2 class="owner">MARCUS OBRIDGE</h2>
    <p class="tagline">Custom modern hair design and custom color</p>

    <ul class="contacts">
      <li><svg viewBox="0 0 16 16"><path d="M8 0a5.5 5.5 0 0 0-5.5 5.5C2.5 10 8 16 8 16s5.5-6 5.5-10.5A5.5 5.5 0 0 0 8 0zm0 8a2.5 2.5 0 1 1 0-5 2.5 2.5 0 0 1 0 5z"/></svg>3182 W 9th St Scottsdale Az 85619</li>
      <li><svg viewBox="0 0 16 16"><path d="M3.6 1l2.6 3.2-1.6 1.9a10 10 0 0 0 5.3 5.3l1.9-1.6L15 12.4 13.2 15C6.8 15 1 9.2 1 2.8z"/></svg>602-4168203</li>
      <li><svg viewBox="0 0 16 16"><path d="M2.6 3l2.2 2.7-1.3 1.6a8.5 8.5 0 0 0 4.5 4.5l1.6-1.3L12.3 12.7 10.8 15C5.4 15 1 10.6 1 5.2zM9 1a6 6 0 0 1 6 6h-1.5A4.5 4.5 0 0 0 9 2.5zm0 3a3 3 0 0 1 3 3h-1.5A1.5 1.5 0 0 0 9 5.5z"/></svg>cell salon 480 -712-6084</li>
      <li><svg viewBox="0 0 16 16"><path d="M1 6l7-5 7 5v9H1zm1.5 1.2V13.5h11V7.2L8 11z"/></svg>marcusobridge@quillpost.com</li>
    </ul>

    <div class="hours">
      <p class="hours__time"><b>7</b>am - <b>6</b>pm</p>
      <p class="hours__days">hours <b>wed.</b> thru. <b>sat.</b></p>
    </div>

    <div class="appointment">
      <p class="appointment__title">APPOINTMENTS:</p>
      <span class="appointment__label">DATE:</span>
      <div class="appointment__field"></div>
      <span class="appointment__label">TIME:</span>
      <div class="appointment__field"></div>
    </div>
  </section>
</body>
</html>
```